Law firm business card

Information:

Me Miriam Dufresne

website: dufresne-law.ca
email: miriam@dufresne-law.ca
Phone: 514 555-0147
Fax: 514 555-0183

Address:
Dufresne and associates
2719 Belcourt
Montreal, QC
H2K 3M9

Areas of Expertise:
Franchise Agreements, Financing, Acquisition, Real Estate Development, Commercial Agreements and Corporate Law

Target Market(s)

executives, companie managers

Industry/Entity Type

Business

Colors
f78f20
000000

Requirements
Must have
• Must use the logo, the logo is available here:

https://www.filebinder-example.com/sh/qxt8rr2ka41wpe/BBKtm7Lwzve_pQRYdNG_HJcWb

```html
<!DOCTYPE html>
<html lang="en">
<head>
<meta charset="utf-8">
<title>Dufresne &amp; Associates – Business Card</title>
<link rel="stylesheet" href="https://fonts.googleapis.com/css2?family=Michroma&family=Montserrat:wght@400;500&display=swap">
<style>
  :root {
    --brand-orange: #f78f20;
    --ink: #000000;
    --ink-soft: #4a4a4a;
    --rule-gold: #b8a27a;
    --card: #ffffff;
    --backdrop: #e6e7ea;
  }
  * { box-sizing: border-box; margin: 0; padding: 0; }
  html, body { width: 1052px; height: 1200px; overflow: hidden; }
  body {
    background: var(--backdrop);
    font-family: "Montserrat", Arial, sans-serif;
    position: relative;
  }
  .card {
    position: absolute;
    left: 76px;
    width: 900px;
    height: 514px;
    background: var(--card);
    box-shadow: 0 6px 18px rgba(0,0,0,0.12);
    overflow: hidden;
  }
  .card--front { top: 60px; }
  .card--back { top: 626px; }

  /* Firm name wordmark: one font, one weight, one colour */
  .firm-name {
    font-family: "Montserrat", Arial, sans-serif;
    font-weight: 500;
    color: var(--brand-orange);
    letter-spacing: 3px;
    line-height: 1.25;
    text-transform: uppercase;
  }
  .firm-square {
    width: 18px; height: 18px;
    background: var(--ink-soft);
    flex: none;
  }

  /* Front */
  .front-brand {
    position: absolute;
    inset: 0;
    display: flex;
    align-items: center;
    justify-content: center;
    gap: 22px;
  }
  .front-brand .firm-name { font-size: 34px; }

  /* Back */
  .holder {
    position: absolute;
    left: 58px; top: 128px;
  }
  .holder__name {
    font-family: "Michroma", Arial, sans-serif;
    font-size: 26px;
    color: var(--ink-soft);
    letter-spacing: 1px;
  }
  .holder__title {
    font-family: "Michroma", Arial, sans-serif;
    font-size: 15px;
    color: var(--ink);
    letter-spacing: 2px;
    margin-top: 10px;
  }
  .holder-rule {
    position: absolute;
    left: 0; top: 224px;
    width: 430px; height: 2px;
    background: var(--rule-gold);
  }
  .back-brand {
    position: absolute;
    left: 520px; top: 110px;
    width: 340px;
    display: flex;
    flex-direction: column;
    align-items: center;
    gap: 18px;
  }
  .back-brand .firm-name { font-size: 32px; text-align: center; }

  .contact-tab {
    position: absolute;
    left: 0; top: 340px;
    width: 92px; height: 174px;
    background: var(--brand-orange);
  }
  .contact-icon {
    position: absolute;
    left: 34px;
    width: 22px; height: 22px;
  }
  .contact-list {
    position: absolute;
    left: 116px; top: 346px;
    list-style: none;
    font-size: 16px;
    color: var(--ink);
    letter-spacing: 0.5px;
  }
  .contact-list li { height: 30px; line-height: 30px; }
  .contact-list .contact-address { margin-top: 22px; line-height: 24px; height: auto; }
</style>
</head>
<body>

<section class="card card--front">
  <div class="front-brand">
    <div class="firm-square"></div>
    <p class="firm-name">Dufresne &amp; Associates</p>
  </div>
</section>

<section class="card card--back">
  <div class="holder">
    <p class="holder__name">MIRIAM DUFRESNE</p>
    <p class="holder__title">GENERAL MANAGER</p>
  </div>
  <div class="holder-rule"></div>

  <div class="back-brand">
    <div class="firm-square"></div>
    <p class="firm-name">Dufresne<br>&amp; Associates</p>
  </div>

  <div class="contact-tab">
    <svg class="contact-icon" style="top:10px" viewBox="0 0 24 24" aria-label="Phone">
      <path fill="#fff" d="M6.6 10.8a15.1 15.1 0 0 0 6.6 6.6l2.2-2.2a1 1 0 0 1 1-.25 11.4 11.4 0 0 0 3.6.57 1 1 0 0 1 1 1V20a1 1 0 0 1-1 1A17 17 0 0 1 3 4a1 1 0 0 1 1-1h3.5a1 1 0 0 1 1 1c0 1.25.2 2.45.57 3.57a1 1 0 0 1-.25 1z"/>
    </svg>
    <svg class="contact-icon" style="top:42px" viewBox="0 0 24 24" aria-label="Email">
      <rect x="2" y="5" width="20" height="14" rx="1.5" fill="#fff"/>
      <path d="M3 6l9 7 9-7" fill="none" stroke="#f78f20" stroke-width="1.6"/>
    </svg>
    <svg class="contact-icon" style="top:74px" viewBox="0 0 24 24" aria-label="Website">
      <g fill="none" stroke="#fff" stroke-width="1.8">
        <circle cx="12" cy="12" r="9"/>
        <ellipse cx="12" cy="12" rx="4" ry="9"/>
        <path d="M3 12h18M5 7h14M5 17h14"/>
      </g>
    </svg>
    <svg class="contact-icon" style="top:132px" viewBox="0 0 24 24" aria-label="Address">
      <path fill="#fff" d="M12 2a7 7 0 0 0-7 7c0 5.2 7 13 7 13s7-7.8 7-13a7 7 0 0 0-7-7zm0 9.5A2.5 2.5 0 1 1 12 6.5a2.5 2.5 0 0 1 0 5z"/>
    </svg>
  </div>

  <ul class="contact-list">
    <li>514 555-0147</li>
    <li>miriam@dufresne-law.ca</li>
    <li>www.dufresne-law.ca</li>
    <li class="contact-address">2719 Belcourt, Montreal, QC<br>H2K 3M9</li>
  </ul>
</section>

</body>
</html>
```